K. Talbin Company Business Card

We are looking for a business card mock-up.

Contact Information for Business Card

This is the information that needs to be included:
Name
Title
The K. Talbin Company Inc. Insurance Agents & Brokers (needs to be listed out in entirety)
Logo
License 0381264 (needs to be same sized font as phone number)
Address (527 West Orchard Avenue, Los Angeles, CA 90018)
Telephone number ( 714-839-2046 ext. 207)Fax number (714-839-6153)
Email
Website (www.ktalbinagency.example)
Cities (Anaheim, Los Angeles, San Jose, Torrance)

```html
<!DOCTYPE html>
<html lang="en">
<head>
<meta charset="utf-8">
<title>K. Talbin Company Business Card</title>
<link href="https://fonts.googleapis.com/css2?family=Cinzel:wght@500&family=Crimson+Text:wght@400;600&family=Open+Sans:wght@400&display=swap" rel="stylesheet">
<style>
  :root {
    --backdrop: #e4e4e4;
    --copper: #a05e2c;
    --copper-deep: #8f5024;
    --card-white: #fbfbfa;
    --ink: #2a2622;
    --white: #ffffff;
    --faint-on-copper: rgba(70, 35, 10, 0.14);
    --faint-on-white: rgba(0, 0, 0, 0.045);
  }
  * { box-sizing: border-box; margin: 0; padding: 0; }
  html, body { width: 1200px; height: 852px; overflow: hidden; }
  body {
    background: var(--backdrop);
    position: relative;
    font-family: "Crimson Text", Georgia, serif;
  }
  .card {
    position: absolute;
    top: 272px;
    width: 540px;
    height: 309px;
    border-radius: 18px;
    overflow: hidden;
    box-shadow: 0 6px 18px rgba(0,0,0,0.18);
  }
  .card-front {
    left: 40px;
    background: linear-gradient(160deg, var(--copper) 0%, var(--copper-deep) 100%);
    color: var(--white);
  }
  .card-back {
    left: 620px;
    background: var(--card-white);
    color: var(--ink);
  }
  .backdrop-circle {
    position: absolute;
    border-radius: 50%;
  }
  .card-front .backdrop-circle {
    width: 300px; height: 300px; right: -40px; top: -70px;
    background: var(--faint-on-copper);
  }
  .card-back .backdrop-circle {
    width: 300px; height: 300px; right: -50px; top: -40px;
    background: var(--faint-on-white);
  }
  .brand {
    position: absolute;
    display: flex;
    align-items: center;
    gap: 12px;
    font-family: "Cinzel", "Times New Roman", serif;
    font-weight: 500;
    white-space: nowrap;
  }
  .brand-dot {
    border-radius: 50%;
    flex: none;
  }
  .card-front .brand { left: 48px; top: 126px; font-size: 31px; color: var(--white); }
  .card-front .brand-dot { width: 52px; height: 52px; background: var(--white); }
  .card-back .brand { left: 30px; top: 34px; font-size: 23px; color: var(--ink); }
  .card-back .brand-dot { width: 40px; height: 40px; background: var(--copper); }
  .legal-name {
    position: absolute;
    left: 34px; top: 86px;
    font-family: "Open Sans", Arial, sans-serif;
    font-size: 10.5px;
    letter-spacing: 1.2px;
    text-transform: uppercase;
    color: var(--ink);
    white-space: nowrap;
  }
  .cities {
    position: absolute;
    left: 0; right: 0; bottom: 30px;
    text-align: center;
    font-family: "Open Sans", Arial, sans-serif;
    font-size: 13px;
    letter-spacing: 0.3px;
  }
  .divider {
    position: absolute;
    left: 232px; right: 24px; top: 142px;
    height: 1.5px;
    background: var(--copper);
  }
  .address {
    position: absolute;
    right: 26px; top: 156px;
    text-align: right;
    font-size: 14px;
    line-height: 1.3;
  }
  .person {
    position: absolute;
    left: 34px; top: 130px;
  }
  .person-name {
    font-family: "Cinzel", "Times New Roman", serif;
    color: var(--copper);
    font-size: 19px;
    font-weight: 500;
  }
  .person-title { font-size: 14px; margin-top: 1px; }
  .contacts {
    position: absolute;
    left: 34px; top: 188px;
    list-style: none;
    font-size: 14px;
    line-height: 1.22;
  }
  .contacts li { display: flex; align-items: center; gap: 10px; }
  .contacts svg { width: 11px; height: 11px; fill: var(--copper); flex: none; }
</style>
</head>
<body>
  <section class="card card-front">
    <div class="backdrop-circle"></div>
    <div class="brand"><span class="brand-dot"></span>K. Talbin Company</div>
    <p class="cities">Anaheim &nbsp;|&nbsp; Los Angeles &nbsp;|&nbsp; San Jose &nbsp;|&nbsp; Torrance</p>
  </section>

  <section class="card card-back">
    <div class="backdrop-circle"></div>
    <div class="brand"><span class="brand-dot"></span>K. Talbin Company</div>
    <p class="legal-name">The K. Talbin Company Inc. &middot; Insurance Agents &amp; Brokers</p>
    <div class="divider"></div>
    <p class="address">527 West Orchard Avenue,<br>Los Angeles, CA 90018<br>License 0381264</p>
    <div class="person">
      <p class="person-name">Kerry Talbin</p>
      <p class="person-title">Managing Director</p>
    </div>
    <ul class="contacts">
      <li><svg viewBox="0 0 12 12"><path d="M1 3c0-1 1-2 2-2l1.5 2.5-1 1c.6 1.4 1.6 2.4 3 3l1-1L11 8c0 1-1 2-2 2C5 10 2 7 1 3z"/></svg>714-839-6153</li>
      <li><svg viewBox="0 0 12 12"><path d="M6 0a6 6 0 110 12A6 6 0 016 0zm0 1.5a4.5 4.5 0 100 9 4.5 4.5 0 000-9zM4 4l1 .2.5 1.3-.6.5c.3.6.7 1 1.3 1.3l.5-.6 1.3.5L8 8c-2.3 0-4-1.7-4-4z"/></svg>714-839-2046 ext. 207</li>
      <li><svg viewBox="0 0 12 12"><path d="M0 2h12v8H0zm1 1v.3l5 3.2 5-3.2V3zm0 1.5V9h10V4.5L6 7.7z"/></svg>ktalbin@ktalbinagency.example</li>
      <li><svg viewBox="0 0 12 12"><path d="M6 0a6 6 0 110 12A6 6 0 016 0zM1.1 5.4h2.3c.1-1.6.5-3 1.1-4A4.9 4.9 0 001.1 5.4zm0 1.2a4.9 4.9 0 003.4 4c-.6-1-1-2.4-1.1-4zm3.5 0c.1 1.8.7 3.4 1.4 4.2.7-.8 1.3-2.4 1.4-4.2zm0-1.2h2.8C7.3 3.6 6.7 2 6 1.2 5.3 2 4.7 3.6 4.6 5.4zm4 0h2.3a4.9 4.9 0 00-3.4-4c.6 1 1 2.4 1.1 4zm0 1.2c-.1 1.6-.5 3-1.1 4a4.9 4.9 0 003.4-4z"/></svg>www.ktalbinagency.example</li>
    </ul>
  </section>
</body>
</html>
```